Business Cards & Stationary Levy Appeal Counsel Partners
Business Cards & Stationary
Business Cards & Stationary Levy Appeal Counsel Partners  - Law
Creative Brief
Professional
Nora Bastable
Attorney
27480 Heron Bluff Boulevard, #200 Leawood, Kansas 66389
Nbastable@lacp-mail.net
LACP-mail.net
The card will need to have our logo on it and the tag line: Member, National Assessment Dispute Alliance

```html
<!DOCTYPE html>
<html lang="en">
<head>
<meta charset="utf-8">
<title>Levy Appeal Counsel Partners – Business Cards</title>
<link href="https://fonts.googleapis.com/css2?family=Arimo:wght@400;700&display=swap" rel="stylesheet">
<style>
  :root{
    --bg:#e9e7e4;
    --card:#ffffff;
    --navy:#17233f;
    --blue:#1f5aa6;
    --ink:#3a3d42;
    --muted:#8b8f96;
    --rule:#9aa0a8;
  }
  *{box-sizing:border-box;margin:0;padding:0}
  html,body{width:1200px;height:852px;overflow:hidden}
  body{background:var(--bg);font-family:"Arimo",Arial,sans-serif;color:var(--ink);position:relative}

  .card{position:absolute;width:500px;height:286px;background:var(--card);border-radius:16px;overflow:hidden;box-shadow:0 6px 18px rgba(0,0,0,.18)}
  .card--stacked{left:80px;top:140px}
  .card--split{left:620px;top:420px}

  .brand{position:absolute;text-align:center;color:var(--navy)}
  .brand__name{display:flex;align-items:center;justify-content:center;gap:8px;font-weight:700;font-size:19px;line-height:1.15;color:var(--navy)}
  .brand__mark{width:12px;height:12px;background:var(--blue);flex:none}
  .brand__tagline{margin-top:6px;font-size:7.5px;letter-spacing:.6px;text-transform:uppercase;color:var(--muted);white-space:nowrap}

  .person__name{font-weight:700;font-size:15px;color:var(--blue)}
  .person__title{font-size:11px;margin-top:3px;color:var(--ink)}
  .address{font-size:11.5px;line-height:1.5;color:var(--ink);white-space:nowrap}
  .divider{position:absolute;width:1px;background:var(--rule)}
  .contacts{position:absolute;list-style:none;font-size:11.5px;line-height:1}
  .contacts li{display:flex;align-items:center;gap:7px;height:17px;white-space:nowrap}
  .contacts svg{width:11px;height:11px;flex:none;fill:var(--ink)}
  .swoosh{position:absolute;left:0;bottom:0;width:500px;height:90px}

  /* stacked card */
  .card--stacked .brand{left:0;right:0;top:34px}
  .card--stacked .person{position:absolute;right:228px;top:108px;text-align:right}
  .card--stacked .address{position:absolute;right:228px;top:170px;text-align:right}
  .card--stacked .divider{left:282px;top:104px;height:110px}
  .card--stacked .contacts{left:292px;top:104px}

  /* split card */
  .card--split .person{position:absolute;left:260px;top:40px}
  .card--split .address{position:absolute;left:260px;top:84px}
  .card--split .contacts{left:260px;top:124px}
  .card--split .divider{left:246px;top:40px;height:165px}
  .card--split .brand{left:12px;width:226px;top:148px}
  .card--split .brand__name{font-size:15px}
  .card--split .brand__tagline{font-size:6.8px;letter-spacing:.4px}
</style>
</head>
<body>

<svg width="0" height="0" style="position:absolute">
  <defs>
    <linearGradient id="silverBand" x1="0" y1="0" x2="1" y2="0">
      <stop offset="0" stop-color="#f4f5f6"/>
      <stop offset=".5" stop-color="#b9bcc2"/>
      <stop offset="1" stop-color="#e3e5e8"/>
    </linearGradient>
    <linearGradient id="blueBand" x1="0" y1="0" x2="1" y2="0">
      <stop offset="0" stop-color="#0d3b7a"/>
      <stop offset=".55" stop-color="#2f73c9"/>
      <stop offset="1" stop-color="#0d3b7a"/>
    </linearGradient>
    <symbol id="icon-phone" viewBox="0 0 24 24"><path d="M6.6 10.8a15 15 0 0 0 6.6 6.6l2.2-2.2a1 1 0 0 1 1-.25 11.4 11.4 0 0 0 3.6.57 1 1 0 0 1 1 1V20a1 1 0 0 1-1 1A17 17 0 0 1 3 4a1 1 0 0 1 1-1h3.5a1 1 0 0 1 1 1c0 1.25.2 2.45.57 3.57a1 1 0 0 1-.25 1z"/></symbol>
    <symbol id="icon-mobile" viewBox="0 0 24 24"><path d="M7 1h10a2 2 0 0 1 2 2v18a2 2 0 0 1-2 2H7a2 2 0 0 1-2-2V3a2 2 0 0 1 2-2zm0 3v14h10V4zm5 15.5a1 1 0 1 0 0 2 1 1 0 0 0 0-2z"/></symbol>
    <symbol id="icon-fax" viewBox="0 0 24 24"><path d="M6 2h10l2 2v5H6zM3 10h18a1 1 0 0 1 1 1v9a1 1 0 0 1-1 1H3a1 1 0 0 1-1-1v-9a1 1 0 0 1 1-1zm3 3v2h2v-2zm4 0v2h2v-2zm4 0v2h2v-2z"/></symbol>
    <symbol id="icon-mail" viewBox="0 0 24 24"><path d="M2 5h20v14H2zm2 2v.5l8 5 8-5V7zm0 3v7h16v-7l-8 5z"/></symbol>
    <symbol id="icon-web" viewBox="0 0 24 24"><path d="M12 2a10 10 0 1 0 0 20 10 10 0 0 0 0-20zm0 3a7 7 0 0 1 6.9 6H16a11 11 0 0 0-1.5-5.5A7 7 0 0 1 12 5zm0 0c1 1.3 1.8 3.5 2 6h-4c.2-2.5 1-4.7 2-6zM5.1 13H8a11 11 0 0 0 1.5 5.5A7 7 0 0 1 5.1 13zm4.9 0h4c-.2 2.5-1 4.7-2 6-1-1.3-1.8-3.5-2-6zm6 0h2.9a7 7 0 0 1-4.4 5.5A11 11 0 0 0 16 13zM5.1 11A7 7 0 0 1 9.5 5.5 11 11 0 0 0 8 11z"/></symbol>
  </defs>
</svg>

<article class="card card--stacked">
  <header class="brand">
    <div class="brand__name"><span class="brand__mark"></span>Levy Appeal Counsel Partners</div>
    <div class="brand__tagline">Member, National Assessment Dispute Alliance</div>
  </header>
  <div class="person">
    <div class="person__name">Nora Bastable</div>
    <div class="person__title">Attorney</div>
  </div>
  <p class="address">27480 Heron Bluff Boulevard,<br>#200, Leawood, Kansas 66389</p>
  <div class="divider"></div>
  <ul class="contacts">
    <li><svg><use href="#icon-phone"/></svg>913-555-0142</li>
    <li><svg><use href="#icon-mobile"/></svg>913-555-0187</li>
    <li><svg><use href="#icon-fax"/></svg>913-555-0163</li>
    <li><svg><use href="#icon-mail"/></svg>Nbastable@lacp-mail.net</li>
    <li><svg><use href="#icon-web"/></svg>www.LACP-mail.net</li>
  </ul>
  <svg class="swoosh" viewBox="0 0 500 90" preserveAspectRatio="none">
    <path d="M0 40 C150 78 330 70 500 20 L500 90 L0 90 Z" fill="url(#silverBand)"/>
    <path d="M0 62 C160 90 330 78 500 36 L500 90 L0 90 Z" fill="url(#blueBand)"/>
    <path d="M0 76 C170 96 340 86 500 56 L500 90 L0 90 Z" fill="#ffffff" opacity=".9"/>
  </svg>
</article>

<article class="card card--split">
  <div class="person">
    <div class="person__name">Nora Bastable</div>
    <div class="person__title">Attorney</div>
  </div>
  <p class="address">27480 Heron Bluff Boulevard,<br>#200, Leawood, Kansas 66389</p>
  <div class="divider"></div>
  <ul class="contacts">
    <li><svg><use href="#icon-phone"/></svg>913-555-0142</li>
    <li><svg><use href="#icon-mobile"/></svg>913-555-0187</li>
    <li><svg><use href="#icon-fax"/></svg>913-555-0163</li>
    <li><svg><use href="#icon-mail"/></svg>Nbastable@lacp-mail.net</li>
    <li><svg><use href="#icon-web"/></svg>www.LACP-mail.net</li>
  </ul>
  <header class="brand">
    <div class="brand__name"><span class="brand__mark"></span>Levy Appeal Counsel<br>Partners</div>
    <div class="brand__tagline">Member, National Assessment Dispute Alliance</div>
  </header>
  <svg class="swoosh" viewBox="0 0 500 90" preserveAspectRatio="none">
    <path d="M0 58 C170 30 340 28 500 50 L500 90 L0 90 Z" fill="url(#silverBand)"/>
    <path d="M0 70 C170 46 340 46 500 64 L500 90 L0 90 Z" fill="url(#blueBand)"/>
    <path d="M0 82 C170 62 340 62 500 78 L500 90 L0 90 Z" fill="#ffffff" opacity=".9"/>
  </svg>
</article>

</body>
</html>
```